TRVA Banner

This is for a generic retractable banner to be used anytime our group goes to large conferences and meetings. Please do not use any of the pictures from our website or reference Chicago or any of the events are attending. The plan is to use this banner anytime we go to a conference, set up at career fairs and have a table at a meeting.
We are the Broadfield Surgical Insights Network (TRVA) and I have included our logo. The website is: www.trva-example.org
Below are some qualities about our group, but please do not use these as a bullet point list on the banner. These are an overview of what we do at TRVA:
- Anesthesiologists / Anesthesiology
- Research, Quality and Education
- Large data repository
- Quality Champions
- Medical Researchers
- Perioperative Outcomes
- Innovators and trailblazers
- Medical research

```html
<!DOCTYPE html>
<html lang="en">
<head>
<meta charset="utf-8">
<title>TRVA Banner</title>
<link rel="stylesheet" href="https://fonts.googleapis.com/css2?family=Ubuntu:wght@400;500;700&family=Montserrat:wght@600;700&display=swap">
<style>
  :root {
    --navy: #1b3a5f;
    --green: #74a22f;
    --orange: #e37a1f;
    --white: #ffffff;
    --grey: #4d4d4d;
    --backdrop: #ececec;
    --badge: #111111;
    --partner-blue: #0a5aa8;
    --partner-gold: #f2c400;
  }
  * { box-sizing: border-box; margin: 0; padding: 0; }
  html, body { width: 1200px; height: 1200px; overflow: hidden; }
  body {
    background: var(--backdrop);
    font-family: "Ubuntu", sans-serif;
    position: relative;
  }
  .banner {
    position: absolute;
    left: 367px; top: 30px;
    width: 465px; height: 1140px;
    background: var(--navy);
    overflow: hidden;
    box-shadow: 0 4px 14px rgba(0,0,0,0.18);
  }
  .banner-header {
    position: absolute; left: 0; top: 0;
    width: 465px; height: 150px;
    background: var(--white);
    text-align: center;
    padding-top: 30px;
  }
  .brand-name {
    display: inline-flex; align-items: center; gap: 14px;
    font-family: "Montserrat", sans-serif;
    font-weight: 700; font-size: 58px; letter-spacing: 10px;
    color: var(--navy); line-height: 1;
  }
  .brand-mark {
    width: 30px; height: 30px; border-radius: 50%;
    background: var(--navy);
  }
  .brand-tagline {
    margin: 10px auto 0; width: 320px;
    font-family: "Montserrat", sans-serif;
    font-weight: 600; font-size: 15px; letter-spacing: 0.5px;
    color: var(--grey); line-height: 1.35; text-transform: uppercase;
  }
  .feature-area {
    position: absolute; left: 0; top: 150px;
    width: 465px; height: 350px;
    background: linear-gradient(90deg, var(--green) 0%, var(--green) 35%, var(--orange) 65%, var(--orange) 100%);
  }
  .qualities {
    position: absolute; top: 528px; left: 0; right: 0;
    list-style: none; text-align: center;
    color: var(--white); font-weight: 500; font-size: 22px;
  }
  .qualities li { height: 39.5px; line-height: 39.5px; }
  .store-badges {
    position: absolute; top: 870px; left: 82px;
    display: flex; gap: 14px;
  }
  .store-badge {
    width: 144px; height: 47px; border-radius: 6px;
    background: var(--badge); border: 1px solid #555;
    display: flex; align-items: center; justify-content: center; gap: 8px;
    color: var(--white); font-size: 20px; font-weight: 500;
  }
  .store-badge .dot { width: 16px; height: 16px; border-radius: 50%; background: var(--white); }
  .partners {
    position: absolute; top: 932px; left: 0;
    width: 465px; height: 136px;
    background: var(--white);
    border-top: 3px solid var(--white);
    display: flex; align-items: center; justify-content: space-between;
    padding: 0 22px 0 26px;
  }
  .partner { display: flex; align-items: center; gap: 10px; }
  .partner-square { width: 40px; height: 40px; background: var(--partner-blue); }
  .partner-square.gold { background: var(--partner-gold); }
  .partner-name {
    font-size: 16px; font-weight: 700; color: var(--partner-blue); line-height: 1.15;
  }
  .partner-name.navy { color: var(--navy); font-size: 13px; }
  .web-address {
    position: absolute; left: 0; right: 0; top: 1068px; height: 72px;
    line-height: 72px; text-align: center;
    color: var(--white); font-weight: 700; font-size: 27px;
  }
</style>
</head>
<body>
  <section class="banner">
    <header class="banner-header">
      <div class="brand-name"><span class="brand-mark"></span>TRVA</div>
      <p class="brand-tagline">Broadfield Surgical Insights Network</p>
    </header>

    <div class="feature-area" role="img" aria-label="Large green and orange feature graphic"></div>

    <ul class="qualities">
      <li>Anesthesiologists / Anesthesiology</li>
      <li>Research, Quality and Education</li>
      <li>Large data repository</li>
      <li>Quality Champions</li>
      <li>Medical Researchers</li>
      <li>Perioperative Outcomes</li>
      <li>Innovators and trailblazers</li>
      <li>Medical research</li>
    </ul>

    <div class="store-badges">
      <div class="store-badge"><span class="dot"></span>AppNest</div>
      <div class="store-badge"><span class="dot"></span>PlayDock</div>
    </div>

    <div class="partners">
      <div class="partner">
        <span class="partner-square"></span>
        <span class="partner-name">Lakeshore<br>Health Plan</span>
      </div>
      <div class="partner">
        <span class="partner-square gold"></span>
        <span class="partner-name navy">DEPARTMENT OF<br>ANESTHESIOLOGY<br>NORTHVALE UNIVERSITY</span>
      </div>
    </div>

    <div class="web-address">www.trva-example.org</div>
  </section>
</body>
</html>
```